We Need a Letterhead + Fax Cover Sheet for Heron Staffing

LETTERHEAD:
- Simple letterhead. Please provide an editable .doc file apart from usual Source Files. Logo Files attached for your use.
- Please place our logo on the upper right corner of the page. You may add some sort of graphic, or light colored background (depends on what looks good).
- Footer should include:
Heron Staffing, LLC
412 Kestrel Ave. Suite 118
Mobile, AL 36619

FAX COVER SHEET:
- Have the logo placed here, should be large, maybe an eight of the page.
- Put:
From:
To:
Phone Number:
Fax Number:

*Still needs some details, will update you because working on the website, etc.

Heron Coastal Workforce Services

```html
<!DOCTYPE html>
<html lang="en">
<head>
<meta charset="utf-8">
<title>Heron Staffing — Fax Cover Sheet and Letterhead</title>
<link href="https://fonts.googleapis.com/css2?family=Open+Sans:wght@400;600&display=swap" rel="stylesheet">
<style>
  :root{
    --bg-top:#fbfbfb;
    --bg-bottom:#c9c9c9;
    --green:#8ba63c;
    --green-tint:#e2e8cf;
    --blue:#0f74b8;
    --ink:#3c3c3c;
    --label:#1e1e1e;
    --white:#ffffff;
  }
  *{box-sizing:border-box;margin:0;padding:0}
  html,body{width:1200px;height:1200px;overflow:hidden}
  body{
    position:relative;
    background:linear-gradient(180deg,var(--bg-top) 0%,#ececec 40%,var(--bg-bottom) 100%);
    font-family:"Open Sans",sans-serif;
    color:var(--ink);
  }
  .sheet{
    position:absolute;
    background:linear-gradient(180deg,var(--green-tint) 0%,#f6f8ef 22%,var(--white) 45%,var(--white) 70%,#f3f6ea 100%);
    box-shadow:2px 4px 8px rgba(0,0,0,.35);
    overflow:hidden;
  }
  .sheet-backing{
    position:absolute;left:492px;top:254px;width:613px;height:858px;
    background:var(--green);
    box-shadow:2px 4px 8px rgba(0,0,0,.3);
  }
  .letterhead{left:463px;top:228px;width:613px;height:858px}
  .fax-sheet{left:68px;top:120px;width:575px;height:805px}
  .footer-wave{position:absolute;left:0;top:0;width:100%;height:100%}
  .faint-mark{
    position:absolute;border-radius:50%;
    border:10px solid rgba(15,116,184,.05);
    background:rgba(139,166,60,.04);
  }
  .fax-sheet .faint-mark{left:20px;top:500px;width:340px;height:340px}
  .letterhead .faint-mark{left:30px;top:540px;width:340px;height:340px}
  .footer-block{
    position:absolute;right:34px;text-align:right;color:var(--white);
  }
  .footer-name{
    font-weight:600;font-size:16px;padding-bottom:6px;
    border-bottom:1px solid rgba(255,255,255,.35);margin-bottom:8px;
  }
  .footer-line{font-size:14px;line-height:22px;display:flex;justify-content:flex-end;align-items:center;gap:3px}
  .fax-sheet .footer-block{top:703px;width:195px}
  .letterhead .footer-block{top:748px;width:206px}
  .letterhead .footer-name{font-size:17px}
  .letterhead .footer-line{font-size:15px;line-height:24px}
  .brand{
    position:absolute;left:36px;top:38px;width:112px;
    display:flex;align-items:flex-start;gap:6px;
  }
  .brand-dot{flex:none;width:14px;height:14px;border-radius:50%;background:var(--blue);margin-top:3px}
  .brand-name{font-weight:600;font-size:13px;line-height:17px;color:var(--blue)}
  .sheet-title{
    position:absolute;left:0;right:0;top:172px;text-align:center;
    color:var(--green);font-weight:600;font-size:27px;letter-spacing:3.5px;padding-left:10px;
  }
  .field-row{position:absolute;left:44px;right:38px;display:flex;gap:12px;font-size:14px;letter-spacing:.4px}
  .field{flex:1;display:flex;align-items:baseline;gap:5px}
  .field-line{flex:1;border-bottom:2px dotted #6a6a6a;height:1px;transform:translateY(-2px)}
  .caption{position:absolute;font-size:29px;color:var(--label);letter-spacing:.3px}
  .caption-letterhead{left:907px;top:175px}
  .caption-fax{left:68px;top:946px}
</style>
</head>
<body>

<div class="sheet-backing"></div>

<section class="sheet letterhead">
  <div class="faint-mark" role="img" aria-label="Faint brand emblem"></div>
  <svg class="footer-wave" viewBox="0 0 613 858" preserveAspectRatio="none" aria-hidden="true">
    <path d="M0 752 C130 790 250 790 360 746 S540 640 613 638 L613 652 C540 654 450 700 360 752 C250 796 130 798 0 756Z" fill="var(--blue)"/>
    <path d="M0 754 C130 792 250 792 360 748 S540 652 613 652 L613 664 C540 664 450 705 360 754 C250 798 130 796 0 757Z" fill="var(--white)"/>
    <path d="M0 756 C130 794 250 794 360 756 S540 664 613 664 L613 858 L0 858Z" fill="var(--green)"/>
  </svg>
  <div class="footer-block">
    <div class="footer-name">Heron Staffing, LLC</div>
    <div class="footer-line">412 Kestrel Ave.
      <svg width="12" height="14" viewBox="0 0 12 14" aria-hidden="true"><path d="M6 0a5 5 0 0 1 5 5c0 3.5-5 9-5 9S1 8.5 1 5a5 5 0 0 1 5-5z" fill="var(--white)"/><circle cx="6" cy="5" r="2" fill="var(--green)"/></svg>
    </div>
    <div class="footer-line">Suite 118, Mobile, AL 36619</div>
  </div>
</section>

<section class="sheet fax-sheet">
  <div class="brand">
    <span class="brand-dot"></span>
    <span class="brand-name">Heron Coastal Workforce Services</span>
  </div>

  <h1 class="sheet-title">FAX COVER SHEET</h1>

  <div class="field-row" style="top:251px"><div class="field">To <span class="field-line"></span></div></div>
  <div class="field-row" style="top:289px"><div class="field">From <span class="field-line"></span></div></div>
  <div class="field-row" style="top:326px"><div class="field">Re <span class="field-line"></span></div></div>
  <div class="field-row" style="top:383px">
    <div class="field">Fax Number <span class="field-line"></span></div>
    <div class="field" style="flex:.95">Pages <span class="field-line"></span></div>
  </div>
  <div class="field-row" style="top:430px">
    <div class="field" style="flex:1.15">Phone Number <span class="field-line"></span></div>
    <div class="field" style="flex:.85">Date <span class="field-line"></span></div>
  </div>

  <div class="faint-mark" role="img" aria-label="Faint brand emblem"></div>
  <svg class="footer-wave" viewBox="0 0 575 805" preserveAspectRatio="none" aria-hidden="true">
    <path d="M0 703 C120 742 230 742 330 702 S510 600 575 598 L575 612 C510 614 420 656 330 708 C230 748 120 748 0 707Z" fill="var(--blue)"/>
    <path d="M0 705 C120 744 230 744 330 704 S510 612 575 612 L575 623 C510 623 420 663 330 710 C230 750 120 746 0 708Z" fill="var(--white)"/>
    <path d="M0 707 C120 746 230 746 330 712 S510 623 575 623 L575 805 L0 805Z" fill="var(--green)"/>
  </svg>
  <div class="footer-block">
    <div class="footer-name">Heron Staffing, LLC</div>
    <div class="footer-line">412 Kestrel Ave.
      <svg width="11" height="13" viewBox="0 0 12 14" aria-hidden="true"><path d="M6 0a5 5 0 0 1 5 5c0 3.5-5 9-5 9S1 8.5 1 5a5 5 0 0 1 5-5z" fill="var(--white)"/><circle cx="6" cy="5" r="2" fill="var(--green)"/></svg>
    </div>
    <div class="footer-line">Suite 118, Mobile, AL 36619</div>
  </div>
</section>

<p class="caption caption-letterhead">LETTERHEAD</p>
<p class="caption caption-fax">FAX COVER SHEET</p>

</body>
</html>
```